Mental Health & Addiction Podcast Art

Project: Podcast Cover Art / Visual Identity
Podcast Name: The Mending Path
Focus: Recovery from substance use and mental health
Objectives
Create compelling podcast artwork that:
Reflects the themes of hope, healing, and personal growth
Establishes credibility and professionalism
Appeals to individuals seeking recovery resources and support
Maintains strong brand consistency with Larkspur Wellness
Brand Integration Requirements
Logo incorporation: Integrate an element from the Larkspur Wellness Logo—potentially an abstract or partial use of the sun motif
Flexibility: Open to creative interpretations (e.g., sun rays as background texture, sunrise gradient, partial sun as a design accent)
Mandatory: Must adhere to existing Larkspur Wellness brand guidelines (approved color palette, typography, and visual style)

Target Market(s)

United states, people with addiction and mental health disorders.

Industry/Entity Type

Wellness

Font styles to use
Other font styles liked:
• See Brand Guide

Requirements
Must have
• Match brand guide, in corporate elements of the Larkspur Wellness Logo icon

```html
<!DOCTYPE html>
<html lang="en">
<head>
<meta charset="utf-8">
<title>The Mending Path Podcast</title>
<link rel="stylesheet" href="https://fonts.googleapis.com/css2?family=Bebas+Neue&family=Barlow:wght@400;500&display=swap">
<style>
  :root {
    --sky-top: #6d91a7;
    --sky-mid: #b9c7c9;
    --haze: #f4f0e0;
    --glow: #fbe9b8;
    --amber: #efb463;
    --ember: #c4805a;
    --dusk: #8a6a6a;
    --ink: #222222;
    --navy: #062c45;
  }
  * { margin: 0; padding: 0; box-sizing: border-box; }
  html, body {
    width: 1200px;
    height: 1200px;
    overflow: hidden;
  }
  body {
    position: relative;
    background: var(--haze);
  }
  .cover {
    position: relative;
    width: 1200px;
    height: 1200px;
    overflow: hidden;
  }
  .hero-scene {
    position: absolute;
    inset: 0;
    background:
      radial-gradient(circle at 76% 55%, rgba(255, 214, 110, 0.85) 0, rgba(253, 230, 160, 0.45) 14%, rgba(253, 230, 160, 0) 34%),
      linear-gradient(180deg,
        var(--sky-top) 0%,
        var(--sky-mid) 22%,
        var(--haze) 42%,
        var(--glow) 60%,
        var(--amber) 76%,
        var(--ember) 88%,
        var(--dusk) 100%);
  }
  .title {
    position: absolute;
    left: 106px;
    top: 92px;
    font-family: "Bebas Neue", sans-serif;
    font-weight: 400;
    line-height: 1;
  }
  .title span { display: block; }
  .title .lead {
    color: var(--ink);
    font-size: 202px;
    line-height: 166px;
    letter-spacing: 2px;
  }
  .title .main {
    color: var(--navy);
    font-size: 268px;
    line-height: 208px;
    letter-spacing: 2px;
  }
  .brand-mark {
    position: absolute;
    left: 112px;
    top: 738px;
    display: flex;
    align-items: center;
    gap: 22px;
  }
  .brand-mark svg { display: block; }
  .brand-name {
    font-family: "Barlow", sans-serif;
    font-weight: 500;
    font-size: 30px;
    color: var(--navy);
    letter-spacing: 1px;
  }
  .podcast-label {
    position: absolute;
    left: 114px;
    top: 988px;
    font-family: "Barlow", sans-serif;
    font-weight: 400;
    font-size: 50px;
    letter-spacing: 14px;
    color: var(--ink);
  }
</style>
</head>
<body>
  <main class="cover">
    <div class="hero-scene" role="img" aria-label="Photograph: a hiker with a backpack stands atop stone steps on a rocky peak, silhouetted against a golden sunrise sky above the clouds"></div>

    <h1 class="title">
      <span class="lead">The</span>
      <span class="main">Mending</span>
      <span class="main">Path</span>
    </h1>

    <div class="brand-mark">
      <svg width="136" height="136" viewBox="0 0 136 136" aria-hidden="true">
        <circle cx="68" cy="68" r="64" fill="none" stroke="var(--navy)" stroke-width="7"/>
      </svg>
      <span class="brand-name">Larkspur Wellness</span>
    </div>

    <p class="podcast-label">PODCAST</p>
  </main>
</body>
</html>
```